Logo and label lay out for Silver Moss wines

Wine Bottle label for single vineyard on The Mornington Peninsula, Victoria, Australia
Name of Vineyard is “Silver Moss”
(A silver Moss is a common biting ant found in the vineyard.)
The name and vintage of each of the four varieties of wine will need to be included on the label.
We want an instantly recognisable image on the label along with the name Silver Moss.

Target Market(s)

Quality wine for cafes, restaurants and individual’s wine collection

Industry/Entity Type

Vineyard

Logo Text

Silver Moss

Logo styles of interest
Emblem Logo
Abstract Logo
Colors

Designer to choose colors to be used in the design.

Requirements
Must have
• Simple yet stylish image, instantly recognisable .
Nice to have
• Possibly a stylistic image of an ant
Should not have
• Not an overly detailed image.

```html
<!DOCTYPE html>
<html lang="en">
<head>
<meta charset="utf-8">
<title>Silver Moss Chardonnay Label</title>
<link href="https://fonts.googleapis.com/css2?family=Josefin+Sans:wght@300;400;600;700&display=swap" rel="stylesheet">
<style>
  :root {
    --ink: #0a0a0a;
    --paper: #ffffff;
    --cream: #f3eee8;
    --stage: #ffffff;
    --shadow: rgba(0, 0, 0, 0.28);
  }
  * { margin: 0; padding: 0; box-sizing: border-box; }
  html, body {
    width: 960px;
    height: 1200px;
    overflow: hidden;
    background: var(--stage);
    font-family: "Josefin Sans", "Helvetica Neue", Arial, sans-serif;
    color: var(--ink);
  }
  .canvas { position: relative; width: 960px; height: 1200px; }

  /* Dimension guides */
  .dimension-guides { position: absolute; inset: 0; }
  .dimension-label {
    position: absolute;
    font-weight: 300;
    font-size: 20px;
    letter-spacing: 0.22em;
    color: var(--ink);
  }
  .dimension-label--width { left: 412px; top: 104px; }
  .dimension-label--height { left: 780px; top: 632px; }

  /* Label */
  .wine-label {
    position: absolute;
    left: 173px;
    top: 150px;
    width: 566px;
    height: 944px;
    background: var(--paper);
    box-shadow: 0 0 8px var(--shadow);
    overflow: hidden;
  }
  .ant-mark {
    position: absolute;
    left: 381px;
    top: 96px;
    width: 78px;
    height: 88px;
    background: radial-gradient(ellipse at center, #1a1a1a 0%, #1a1a1a 30%, rgba(26,26,26,0.25) 60%, rgba(255,255,255,0) 75%);
  }
  .stripe {
    position: absolute;
    left: 0;
    width: 100%;
    background: var(--ink);
  }
  .stripe--1 { top: 198px; height: 24px; }
  .stripe--2 { top: 254px; height: 32px; }
  .stripe--3 { top: 328px; height: 32px; }
  .stripe--4 { top: 408px; height: 32px; }
  .name-band {
    position: absolute;
    left: 0;
    top: 466px;
    width: 100%;
    height: 234px;
    background: var(--ink);
  }
  .brand-name {
    position: absolute;
    left: 57px;
    top: 72px;
    color: var(--cream);
    font-weight: 600;
    font-size: 40px;
    line-height: 86px;
    letter-spacing: 0.62em;
    text-transform: uppercase;
  }
  .variety {
    position: absolute;
    left: 57px;
    top: 755px;
    font-weight: 600;
    font-size: 29px;
    line-height: 32px;
    letter-spacing: 0.14em;
  }
  .origin {
    position: absolute;
    left: 60px;
    top: 848px;
    font-weight: 600;
    font-size: 20px;
    line-height: 28px;
    letter-spacing: 0.1em;
  }
</style>
</head>
<body>
<div class="canvas">
  <svg class="dimension-guides" width="960" height="1200" viewBox="0 0 960 1200" aria-hidden="true">
    <g stroke="#0a0a0a" stroke-width="3" fill="none">
      <line x1="173" y1="124" x2="368" y2="124"/>
      <line x1="544" y1="124" x2="738" y2="124"/>
      <line x1="174" y1="115" x2="174" y2="133"/>
      <line x1="737" y1="115" x2="737" y2="133"/>
      <line x1="788" y1="151" x2="788" y2="598"/>
      <line x1="788" y1="692" x2="788" y2="1093"/>
      <line x1="779" y1="151" x2="797" y2="151"/>
      <line x1="779" y1="1093" x2="797" y2="1093"/>
    </g>
  </svg>
  <div class="dimension-label dimension-label--width">60MM</div>
  <div class="dimension-label dimension-label--height">100MM</div>

  <div class="wine-label">
    <div class="ant-mark" role="img" aria-label="Black silhouette of an ant walking on the top stripe"></div>
    <div class="stripe stripe--1"></div>
    <div class="stripe stripe--2"></div>
    <div class="stripe stripe--3"></div>
    <div class="stripe stripe--4"></div>
    <div class="name-band">
      <h1 class="brand-name">Silver<br>Moss</h1>
    </div>
    <p class="variety">CHARDONNAY<br>2018</p>
    <p class="origin">SINGLE VINEYARD<br>MORNINGTON PENINSULA</p>
  </div>
</div>
</body>
</html>
```